Marlow Hire Business Card for recruitment company

We are looking for a Business Card Design that incorporates our personal details and our busines name and logo. We are a specialized search consultancy that recruit Property and Construction professionals.
We would like a business card that stands out and is appealing to the Construction and Property industry as well.

Target Market(s)

people in the construction and property industry

Contact Information for Business Card

Business Name and logo

Font styles to use
Serif

Colors
0094D4
00A9DD
6FCCEA
C7EBF8
E9F6FB

Requirements
Must have
• Business name and logo as well as contact details
Should not have
• No photos of us please

```html
<!DOCTYPE html>
<html lang="en">
<head>
<meta charset="utf-8">
<title>Marlow Hire – Business Card</title>
<link rel="stylesheet" href="https://fonts.googleapis.com/css2?family=Roboto+Slab:wght@300;400;700&family=Roboto:wght@500&family=Roboto+Condensed:wght@700&display=swap">
<style>
  :root {
    --navy: #07364f;
    --navy-deep: #053550;
    --pattern-light: #8fa7a8;
    --paper: #ffffff;
    --backdrop: #f2f2f2;
  }
  * { box-sizing: border-box; margin: 0; padding: 0; }
  html, body { width: 1200px; height: 857px; overflow: hidden; }
  body { background: var(--backdrop); position: relative; }

  .card {
    position: absolute;
    top: 111px;
    width: 362px;
    height: 634px;
  }
  .card--front { left: 195px; background: var(--navy); }
  .card--back  { left: 642px; background: var(--navy-deep); }

  .card__panel {
    position: absolute;
    left: 10px; top: 10px; right: 10px;
    height: 559px;
    background: var(--paper);
  }
  .card__frame {
    position: absolute;
    inset: 7px;
    border: 1px solid var(--navy);
  }

  .brand-mark {
    position: absolute;
    left: 151px; top: 75px;
    width: 40px; height: 40px;
    border-radius: 50%;
    background: var(--navy);
  }
  .brand-name {
    position: absolute;
    left: 0; right: 0; top: 196px;
    text-align: center;
    font-family: "Roboto Slab", serif;
    font-weight: 400;
    font-size: 33px;
    letter-spacing: 1px;
    color: var(--navy);
    line-height: 1;
  }

  .person { position: absolute; left: 40px; right: 40px; top: 250px; color: var(--navy); }
  .person__name {
    font-family: "Roboto Slab", serif;
    font-weight: 700;
    font-size: 31px;
    line-height: 1.1;
    text-align: center;
  }
  .person__role {
    margin-top: 3px;
    font-family: "Roboto", sans-serif;
    font-weight: 500;
    font-size: 15.5px;
    text-align: center;
  }

  .divider {
    position: absolute;
    left: 40px; right: 40px; top: 324px;
    border-top: 1.5px solid var(--navy);
  }

  .contact { position: absolute; left: 40px; top: 340px; list-style: none; color: var(--navy);
    font-family: "Roboto Slab", serif; font-weight: 300; font-size: 19px; }
  .contact__item { display: flex; align-items: flex-start; line-height: 30.5px; }
  .contact__icon { width: 22px; height: 26px; margin: 2px 6px 0 0; flex: none; }

  .card__footer {
    position: absolute;
    left: 0; right: 0; bottom: 0; height: 65px;
    display: flex; align-items: center; justify-content: center;
    font-family: "Roboto Condensed", sans-serif;
    font-weight: 700;
    font-size: 23px;
    letter-spacing: 2px;
    color: var(--paper);
  }

  .card__pattern {
    position: absolute; inset: 0;
    background: radial-gradient(ellipse at 50% 50%, #4f6f78 0%, #2a5064 55%, var(--navy-deep) 100%);
  }
</style>
</head>
<body>

  <section class="card card--front">
    <div class="card__panel">
      <div class="card__frame"></div>
      <div class="brand-mark"></div>
      <div class="brand-name">MARLOW HIRE</div>

      <div class="person">
        <h1 class="person__name">Helena Marsh</h1>
        <p class="person__role">Director | Senior Search Consultant</p>
      </div>

      <div class="divider"></div>

      <ul class="contact">
        <li class="contact__item">
          <svg class="contact__icon" viewBox="0 0 22 26" aria-hidden="true">
            <circle cx="11" cy="13" r="10" fill="none" stroke="#07364f" stroke-width="1.5"/>
            <path d="M8 7.5c-1 .6-1.5 1.6-1.2 3 .6 2.6 2.4 5 4.6 6.4 1 .6 2.2.6 3-.2l.6-.6-2.2-1.8-1 .8c-1.2-.7-2.2-2-2.7-3.3l1-.7-1-2.6z" fill="#07364f"/>
          </svg>
          <span>+64 27 480 2915</span>
        </li>
        <li class="contact__item">
          <svg class="contact__icon" viewBox="0 0 22 26" aria-hidden="true">
            <circle cx="11" cy="13" r="10" fill="none" stroke="#07364f" stroke-width="1.5"/>
            <rect x="5" y="9" width="12" height="8" rx="1" fill="#07364f"/>
            <path d="M5.5 9.5 11 13.5l5.5-4" fill="none" stroke="#fff" stroke-width="1"/>
          </svg>
          <span>helena@marlowhire.nz</span>
        </li>
        <li class="contact__item">
          <svg class="contact__icon" viewBox="0 0 22 26" aria-hidden="true">
            <path d="M11 25C5 17 2 13.5 2 10a9 9 0 0 1 18 0c0 3.5-3 7-9 15z" fill="none" stroke="#07364f" stroke-width="1.5"/>
            <circle cx="11" cy="10" r="4" fill="#07364f"/>
          </svg>
          <span>12 Harbour Lane,<br>Northcote, Auckland,<br>0627, New Zealand</span>
        </li>
      </ul>
    </div>
    <div class="card__footer">WWW.MARLOWHIRE.NZ</div>
  </section>

  <section class="card card--back">
    <div class="card__pattern" role="img" aria-label="Repeating brand pattern in pale grey-green on deep navy"></div>
  </section>

</body>
</html>
```